Brookmere Roofing Business Card

This is my current business card. But I’d like to make some changes. Somewhere on the card I’d like to list some of the services we offer. Maybe on the back? But I’d still like to keep the red. White and black modern look.

-residential & commercial roofing
-Roof Repairs & Maintenance
-Storm Damage & Insurance Claims specialist
-Christmas Lights and permanent Christmas lights
Fencing. Windows. Gutters. Siding. Sheetrock, painting.

```html
<!DOCTYPE html>
<html lang="en">
<head>
<meta charset="UTF-8">
<title>Brookmere Roofing Business Card</title>
<link rel="stylesheet" href="https://fonts.googleapis.com/css2?family=Montserrat:wght@400;500&family=Orbitron:wght@800&display=swap">
<style>
  :root {
    --backdrop: #d3d4d6;
    --red: #e0242b;
    --red-deep: #6e0f12;
    --red-mid: #a3161c;
    --black: #111111;
    --white: #ffffff;
    --ink: #1c1c1c;
  }
  * { margin: 0; padding: 0; box-sizing: border-box; }
  html, body { width: 900px; height: 1200px; overflow: hidden; }
  body { background: var(--backdrop); position: relative; font-family: "Montserrat", sans-serif; color: var(--ink); }

  .card { position: absolute; left: 121px; width: 658px; border-radius: 14px; overflow: hidden; }
  .card-front { top: 204px; height: 375px; }
  .card-back { top: 620px; height: 385px; background: var(--white); }

  .tartan-fill {
    position: absolute; inset: 0;
    background:
      linear-gradient(180deg, rgba(0,0,0,0) 0%, rgba(0,0,0,0) 40%, rgba(0,0,0,0.55) 52%, rgba(0,0,0,0.55) 66%, rgba(0,0,0,0) 72%),
      linear-gradient(90deg, var(--red-deep) 0%, var(--red) 25%, var(--red-mid) 50%, var(--red) 75%, var(--red-deep) 100%);
  }

  .brand-mark { position: absolute; border-radius: 50%; }
  .card-front .brand-mark { left: 254px; top: 68px; width: 150px; height: 150px; border: 4px solid var(--white); background: transparent; }
  .card-back .brand-mark { left: 273px; top: 18px; width: 112px; height: 112px; background: var(--red); }

  .brand-name { position: absolute; left: 0; width: 100%; text-align: center; font-family: "Orbitron", sans-serif; font-weight: 800; line-height: 1; }
  .card-front .brand-name { top: 242px; color: var(--white); }
  .card-front .brand-line-1 { font-size: 40px; letter-spacing: 1px; }
  .card-front .brand-line-2 { font-size: 26px; margin-top: 12px; letter-spacing: 1px; }
  .card-back .brand-name { top: 148px; color: var(--red); }
  .card-back .brand-line-1 { font-size: 30px; letter-spacing: 1px; }
  .card-back .brand-line-2 { font-size: 20px; margin-top: 8px; letter-spacing: 1px; }

  .services { position: absolute; right: 350px; top: 230px; list-style: none; text-align: right; font-size: 15px; line-height: 17px; }
  .services li { position: relative; padding-right: 14px; margin-bottom: 6px; }
  .services li::after { content: ""; position: absolute; right: 0; top: 50%; width: 5px; height: 5px; margin-top: -2px; border-radius: 50%; background: var(--red); }

  .divider { position: absolute; left: 325px; top: 226px; width: 2px; height: 126px; background: var(--red); }

  .contact { position: absolute; left: 341px; top: 230px; }
  .person-name { font-family: "Orbitron", sans-serif; font-weight: 800; font-size: 22px; letter-spacing: 1px; color: var(--black); }
  .person-name .surname { color: var(--red); }
  .person-role { font-size: 15px; margin-top: 4px; }
  .contact-list { list-style: none; margin-top: 8px; font-size: 15px; }
  .contact-list li { display: flex; align-items: center; gap: 9px; height: 24px; }
  .contact-list svg { width: 14px; height: 14px; fill: var(--red); flex: none; }

  .tartan-band { position: absolute; left: 0; bottom: 0; width: 100%; height: 22px;
    background: linear-gradient(90deg, var(--red-deep) 0%, var(--red) 20%, var(--red-deep) 45%, var(--red-mid) 70%, var(--red) 85%, var(--red-deep) 100%); }
</style>
</head>
<body>

<section class="card card-front">
  <div class="tartan-fill" role="img" aria-label="Red, black and white tartan plaid pattern"></div>
  <div class="brand-mark"></div>
  <div class="brand-name">
    <div class="brand-line-1">BROOKMERE</div>
    <div class="brand-line-2">ROOFING CO.</div>
  </div>
</section>

<section class="card card-back">
  <div class="brand-mark"></div>
  <div class="brand-name">
    <div class="brand-line-1">BROOKMERE</div>
    <div class="brand-line-2">ROOFING CO.</div>
  </div>

  <ul class="services">
    <li>residential &amp; commercial roofing</li>
    <li>Roof Repairs &amp; Maintenance</li>
    <li>Storm Damage &amp;<br>Insurance Claims specialist</li>
    <li>Fencing. Windows. Gutters.<br>Siding. Sheetrock, painting</li>
  </ul>

  <div class="divider"></div>

  <div class="contact">
    <div class="person-name">DEAN <span class="surname">HARLOW</span></div>
    <div class="person-role">Owner</div>
    <ul class="contact-list">
      <li><svg viewBox="0 0 24 24"><path d="M6.6 10.8c1.4 2.8 3.8 5.1 6.6 6.6l2.2-2.2c.3-.3.7-.4 1-.2 1.1.4 2.3.6 3.6.6.6 0 1 .4 1 1V20c0 .6-.4 1-1 1C10.6 21 3 13.4 3 4c0-.6.4-1 1-1h3.5c.6 0 1 .4 1 1 0 1.3.2 2.5.6 3.6.1.3 0 .7-.2 1z"/></svg>682-555-0143</li>
      <li><svg viewBox="0 0 24 24"><path d="M2 5h20v14H2z M2 5l10 8 10-8" /></svg>dean@brookmereroofing.com</li>
      <li><svg viewBox="0 0 24 24"><circle cx="12" cy="12" r="10"/></svg>www.brookmereroofing.com</li>
    </ul>
  </div>

  <div class="tartan-band" role="img" aria-label="Strip of red, black and white tartan plaid"></div>
</section>

</body>
</html>
```